Pell School of Dental Assisting needs a WP (re)design.

We need a colorful Wordpress design for a relaunch of an old website. The relaunch is already underway and the website is live. The home page URL is brindlecrestacademy.example I have just completed a ArtFlock logo and the new logo is live on the website also. The installed Wordpress theme that is being used is Loomer III Plus with their "Talvek" subtheme. I would like a (re)design using the colors that are currently being represented by the new logo, and any additional complimentary colors. The information regarding the business can be found on the website already, so please review it for insight. The name of the business is "R. Jon Pell School of Dental Assisting".

Target Market(s)

The targeted website viewer is an adult female between the ages of 18 and 30 who is interested in attending our short term 10 week career school. The targeted audience's perception is two fold. Number one, they must have or develop interest in a future healthcare career and number two, they must complete the necessary requirements of our 10 week training course.

This website should inspire in the target viewer both the benefits of dental assistant employment and the essential learning and skills training required. Many of these potential student candidates are desperately wanting to get a job with income.

In addition to the hope of future employment, the website must represent the schools objectives are, classroom education and hands on clinical trainingl. Each webpage must represent both of these meanings to the targeted potential student.

Industry/Entity Type

Business

Font styles to use
Sans Serif

Requirements
Must have
• The phone number placed in a visible and high value widget area that allows mobile phone browser dialing.

```html
<!DOCTYPE html>
<html lang="en">
<head>
<meta charset="utf-8">
<title>R. Jon Pell School of Dental Assisting</title>
<link rel="stylesheet" href="https://fonts.googleapis.com/css2?family=Lato:ital,wght@0,400;0,700;1,400&family=Lobster+Two:ital,wght@0,400;0,700;1,400;1,700&display=swap">
<style>
:root{
  --blue:#1f6fbd;
  --heading-blue:#3a5fcd;
  --green:#009a36;
  --page-grey:#ebebeb;
  --band-grey:#f0f0f0;
  --panel-grey:#f3f3f3;
  --text:#222;
  --muted:#666;
  --social-blue:#3768c9;
}
*{margin:0;padding:0;box-sizing:border-box}
html,body{width:1200px;height:1000px;overflow:hidden}
body{position:relative;font-family:'Lato',sans-serif;color:var(--text);
  background:linear-gradient(to bottom,var(--page-grey) 0,var(--page-grey) 255px,#c9c9c9 256px,#e4e4e4 420px,#fff 560px,#fff 760px)}
.abs{position:absolute}
.top-rule{left:0;top:0;width:1200px;height:5px;background:#1b6fb8}
.top-stripes{left:0;top:5px;width:1200px;height:15px;
  background:repeating-linear-gradient(135deg,#cfe3d4 0 2px,#eef3ef 2px 5px)}
.brand{left:200px;top:30px;width:285px;display:flex;align-items:center;gap:10px}
.brand-mark{width:40px;height:40px;border-radius:50%;background:var(--blue);flex:none}
.brand-name{font-weight:700;font-size:22px;line-height:26px;color:var(--blue)}
.phone{left:760px;top:28px;width:232px;text-align:right;font-size:30px;color:var(--green);text-decoration:none}
.social{display:flex;gap:10px}
.social span{width:40px;height:40px;border-radius:50%;display:block}
.social-top{left:795px;top:66px}
.social-top span{background:var(--green)}
.nav{left:563px;top:114px;display:flex;gap:19px;font-size:17px;color:#333;align-items:center}
.nav a{color:#333;text-decoration:none}
.nav-dot{left:567px;top:143px;width:9px;height:9px;border-radius:50%;background:var(--green)}
.hero{left:192px;top:163px;width:807px;height:255px;background:#fff;border-radius:8px;box-shadow:0 12px 24px rgba(0,0,0,.25)}
.hero-photo{left:605px;top:3px;width:180px;height:252px;border-radius:40px 40px 0 0;background:linear-gradient(#dfe6ee,#c9d3de);z-index:0}
.hero-title{left:36px;top:40px;width:560px;text-align:center;white-space:nowrap;font-family:'Lobster Two',cursive;font-style:italic;font-weight:700;font-size:39px;line-height:46px;color:var(--blue);z-index:1}
.hero-sub{left:0;top:94px;width:630px;text-align:center;font-size:13px;z-index:1}
.hero-join{left:0;top:142px;width:595px;text-align:center;font-size:18px;color:var(--green)}
.hero-input{left:118px;top:175px;width:251px;height:36px;border:1px solid #ccc;font:16px 'Lato',sans-serif;color:#999;padding:8px 12px}
.hero-btn{left:375px;top:175px;width:105px;height:36px;background:var(--green);color:#fff;font-weight:700;font-size:15px;text-align:center;line-height:36px;border-radius:2px}
.section-title{font-family:'Lobster Two',cursive;font-style:italic;font-weight:400;font-size:25px;line-height:30px;color:var(--heading-blue);text-transform:uppercase;white-space:nowrap}
.about-title{left:199px;top:444px}
.school-title{left:512px;top:444px}
.portrait{left:190px;top:492px;width:106px;height:106px;border-radius:50%;background:linear-gradient(#d3d8de,#8c939b);box-shadow:0 4px 6px rgba(0,0,0,.3)}
.about-text{font-size:13.5px;line-height:18px;color:#333}
.about-a{left:309px;top:487px;width:185px}
.about-b{left:201px;top:619px;width:292px}
.pitch{left:506px;top:489px;width:513px;height:259px;background:var(--panel-grey);border-radius:10px;text-align:center;padding:0 10px}
.pitch-tag{font-style:italic;font-size:23px;color:var(--green);line-height:28px}
.pitch p{font-size:13.5px;line-height:20px;margin-top:14px}
.pitch p + p{margin-top:20px}
.pitch-cta{font-style:italic;font-size:23px;line-height:24px;color:var(--green);margin-top:20px}
.testimonials{left:0;top:760px;width:1200px;height:138px;background:var(--band-grey)}
.testi-title{left:195px;top:5px}
.quote-mark{width:46px;height:46px;border-radius:50%;background:var(--green);color:#fff;font:700 38px/58px Georgia,serif;text-align:center}
.quote-open{left:133px;top:49px}
.quote-close{left:1027px;top:62px}
.quote-text{left:180px;top:44px;width:840px;text-align:center;font-size:20px;letter-spacing:.6px;line-height:29px;color:var(--muted);white-space:nowrap}
.quote-name{left:700px;top:105px;width:252px;text-align:right;font-size:20px;letter-spacing:.6px;color:var(--green)}
.footer{left:0;top:898px;width:1200px;height:102px;background:var(--green)}
.foot-nav{left:156px;top:52px;display:flex;gap:12px;font-size:11.5px;color:#fff}
.social-foot{left:519px;top:39px}
.social-foot span{background:var(--social-blue)}
.copyright{left:748px;top:51px;font-size:12px;font-weight:700;color:#fff}
</style>
</head>
<body>
<div class="abs top-rule"></div>
<div class="abs top-stripes"></div>

<header>
  <div class="abs brand">
    <span class="brand-mark"></span>
    <span class="brand-name">R. Jon Pell School of Dental Assisting</span>
  </div>
  <a class="abs phone" href="tel:5550142290">(555) 014-2290</a>
  <div class="abs social social-top" aria-label="Social links"><span></span><span></span><span></span><span></span></div>
  <nav class="abs nav">
    <svg width="14" height="14" viewBox="0 0 14 14" aria-label="Home"><path d="M7 1 L13 7 H11 V13 H8.5 V9 H5.5 V13 H3 V7 H1 Z" fill="#111"/></svg>
    <a href="#" style="margin-left:15px">About Us</a><a href="#">Information</a><a href="#">Resources</a><a href="#">Contact Us</a>
  </nav>
  <div class="abs nav-dot"></div>
</header>

<section class="abs hero">
  <div class="abs hero-photo" role="img" aria-label="Photo of the school director in a white clinical coat, arms crossed"></div>
  <h1 class="abs hero-title">Learn How to Become a Dental Assistant</h1>
  <div class="abs hero-sub">In just 10 Weeks on Saturdays Only – 50% Classroom and 50% Hands On Clinical Training</div>
  <div class="abs hero-join">Join our mailing list &amp; receive information &amp; updates!</div>
  <div class="abs hero-input">Email address...</div>
  <div class="abs hero-btn">SIGN UP</div>
</section>

<h2 class="abs section-title about-title">About R. Jon Pell</h2>
<h2 class="abs section-title school-title">R. Jon Pell School of Dental Assisting</h2>

<div class="abs portrait" role="img" aria-label="Portrait photo of the school director"></div>
<p class="abs about-text about-a">Lorem ipsum dolor sit amet, consectetur adipiscing elit. Suspendisse fermentum sollicitudin libero eget consectetur. Donec eu nulla in erat tincidunt accumsan. Donec semper consequat</p>
<p class="abs about-text about-b">Donec malesuada, enim ut ornare pellentesque, mi enim feugiat enim, molestie scelerisque velit sapien id nisl. Donec ultricies, felis ut mollis aliquet, sapien diam tempus risus, nec pretium ipsum dolor id mi. Donec vitae est ac metus elementum rhoncus et eu nunc. In consectetur fermentum augue, in tincidunt risus dictum sit</p>

<div class="abs pitch">
  <div class="pitch-tag">Your Shortcut to a Meaningful Career!</div>
  <p>Would you believe that in only ten weekends you could learn the necessary skills to become a Dental Assistant?<br>Everywhere in America and abroad, dental assistants jobs are in high demand. &nbsp;In both urban and rural areas dental assistants are being hired and paid well.</p>
  <p>If you are considering a career move, dental assisting may be right for you. &nbsp;Call us today because our next class begins soon and it’s filling up very fast.</p>
  <div class="pitch-cta">Don’t hesitate, call (555) 014-2290 now and sign up today.</div>
</div>

<section class="abs testimonials">
  <h2 class="abs section-title testi-title">Student Testimonials</h2>
  <div class="abs quote-mark quote-open">“</div>
  <div class="abs quote-text">Students, are instructed in fundamental and general dental assisting.<br>I would highly recommend R.JON PELL SCHOOL OF DENTAL ASSISTING</div>
  <div class="abs quote-name">-STUDENT NAME</div>
  <div class="abs quote-mark quote-close">”</div>
</section>

<footer class="abs footer">
  <nav class="abs foot-nav"><span>Home</span><span>About Us</span><span>Information</span><span>Resources</span><span>Contact Us</span></nav>
  <div class="abs social social-foot"><span></span><span></span><span></span><span></span></div>
  <div class="abs copyright">© Copyright 2014 R.Jon Pell School of Dental Assisting.com</div>
</footer>
</body>
</html>
```